Packaging for New Supplement Line

Need a cool, military themed package designed for new supplement line inspired by a retired Navy Seal. Maybe use KRT Mark II camo (example attached) as background and military fonts - just a suggestion maybe you have a way cooler idea? Product name is "DXRT Core Vanguard"
Navy Seal has a logo we'd like featured somewhere small or not "loud" on the package (example attached) Product to be packaged in a "wide mouth" pouch (example attached) but want a small window to view the contents. Contents will be a special vanilla protein powder in clear stickpacks (example attached) The design should reflect military strength cutting edge, superior nutrition.

```html
<!DOCTYPE html>
<html lang="en">
<head>
<meta charset="utf-8">
<title>DXRT Core Vanguard – Special Vanilla Protein Powder</title>
<link rel="stylesheet" href="https://fonts.googleapis.com/css2?family=Exo+2:ital,wght@0,600;0,700;1,800;1,900&display=swap">
<style>
  :root {
    --page-bg: #f5f6f8;
    --camo-light: #cfc9ba;
    --camo-mid: #a9a190;
    --camo-dark: #7a7262;
    --label-fill: #8e8778;
    --label-edge: #b3ac9d;
    --label-inner: #a29b8b;
    --text-white: #ffffff;
    --text-taupe: #d8d2c4;
    --tag-fill: #857e6f;
  }
  * { margin: 0; padding: 0; box-sizing: border-box; }
  html, body {
    width: 1200px; height: 1200px; overflow: hidden;
    background: var(--page-bg);
    font-family: "Exo 2", sans-serif;
  }
  .canvas {
    position: relative; width: 1200px; height: 1200px;
  }
  .pouch-front {
    position: absolute; left: 310px; top: 130px;
    width: 580px; height: 940px;
    overflow: hidden;
  }
  .camo-field {
    position: absolute; inset: 0;
    background:
      radial-gradient(ellipse at 30% 25%, rgba(255,255,255,0.18), transparent 55%),
      linear-gradient(160deg, var(--camo-light) 0%, var(--camo-mid) 45%, var(--camo-dark) 100%);
  }
  .title-plate {
    position: absolute; left: 50px; top: 190px;
    width: 480px; height: 210px;
    background: var(--label-fill);
    border: 6px solid var(--label-edge);
    box-shadow: inset 0 0 0 4px var(--label-inner);
    padding: 22px 34px;
  }
  .brand-line {
    font-style: italic; font-weight: 800;
    font-size: 34px; line-height: 1;
    color: var(--text-taupe);
    letter-spacing: 1px;
  }
  .product-name {
    margin-top: 8px;
    font-style: italic; font-weight: 900;
    font-size: 62px; line-height: 0.98;
    color: var(--text-white);
    text-transform: uppercase;
    letter-spacing: 0.5px;
  }
  .flavour-tag {
    position: absolute; left: 120px; top: 560px;
    width: 340px;
    background: var(--tag-fill);
    border: 4px solid var(--label-edge);
    border-radius: 8px;
    padding: 12px 18px;
    text-align: center;
    font-weight: 700; font-size: 30px; line-height: 1.15;
    color: var(--text-white);
  }
  .team-mark {
    position: absolute; left: 0; right: 0; top: 780px;
    display: flex; align-items: center; justify-content: center; gap: 12px;
  }
  .team-mark-dot {
    width: 22px; height: 22px; border-radius: 50%;
    background: var(--text-white);
  }
  .team-mark-name {
    font-weight: 700; font-size: 30px;
    color: var(--text-white);
    text-transform: uppercase; letter-spacing: 2px;
  }
</style>
</head>
<body>
<main class="canvas">
  <section class="pouch-front">
    <div class="camo-field" role="img" aria-label="Desert camouflage pattern in sand, taupe and dark brown tones"></div>

    <div class="title-plate">
      <p class="brand-line">DXRT</p>
      <h1 class="product-name">Core<br>Vanguard</h1>
    </div>

    <p class="flavour-tag">special vanilla<br>protein powder</p>

    <div class="team-mark">
      <span class="team-mark-dot"></span>
      <span class="team-mark-name">Tidewater Ops</span>
    </div>
  </section>
</main>
</body>
</html>
```